Environmentally friendly Home and Office cleaning service needs a logo and web design!

Tidewell Housekeeping is a new startup looking for a logo and web design. We're base in Ottawa, Canada, and all of our products are eco-friendly, as well as being easy on the sensitivities of our clients.
We wash windows, walls, kitchens, bathrooms, dust, vacuum and wash floors on our hands and knees, and bring all of our own gear and supplies.
plumrake.example was my last website. It's functional, not bad - but just isn't great. I'm looking for a simple design, with few links or clickable buttons.
Colours I will leave to your creative mind to decide. I just want to see something that is relevant to "Tidewell Housekeeping."

Target Market(s)

Often it's women and gay men, ages 35-70
White collar government workers, usually with pets (cats, dogs)

Industry/Entity Type

Cleaning Service

Logo Text

Tidewell Housekeeping

Number of Pages Required

1 page

Font styles to use
Sans Serif

Colors

Designer to choose colors to be used in the design.

Requirements
Must have
• Colour, pictures

```html
<!DOCTYPE html>
<html lang="en">
<head>
<meta charset="utf-8">
<title>Tidewell Housekeeping</title>
<link href="https://fonts.googleapis.com/css2?family=Roboto:ital,wght@0,300;0,400;0,500;0,700;1,400&display=swap" rel="stylesheet">
<style>
:root{
  --green:#8ca322;
  --green-dark:#748a16;
  --ink:#2f2f2f;
  --muted:#6d6d6d;
  --light:#f0f0f0;
  --footer:#3b3b3b;
  --white:#ffffff;
}
*{margin:0;padding:0;box-sizing:border-box}
html,body{width:1200px;height:2839px;overflow:hidden}
body{font-family:'Roboto',sans-serif;color:var(--ink);background:var(--white);position:relative}
section,header,footer{position:absolute;left:0;width:1200px}
.btn{display:inline-block;background:var(--green);color:var(--white);font-size:13px;font-weight:700;letter-spacing:.5px;padding:11px 26px;text-transform:uppercase}
.heading{font-size:21px;font-weight:700;letter-spacing:.5px;text-transform:uppercase}
.small{font-size:12px;line-height:1.6;color:var(--muted)}

/* top strip */
.top-strip{position:absolute;left:0;width:1200px;top:0;height:38px;display:flex;justify-content:flex-end;align-items:center;gap:26px;padding-right:40px;font-size:11px;color:var(--muted)}
.top-strip span{display:flex;align-items:center;gap:6px}
.top-strip i{display:inline-block;width:10px;height:10px;background:var(--green);border-radius:50%}

/* header */
.site-header{top:38px;height:94px;display:flex;align-items:center;justify-content:space-between;padding:0 60px}
.brand{display:flex;align-items:center;gap:10px;font-size:24px;font-weight:700;color:var(--ink)}
.brand-dot{width:16px;height:16px;border-radius:50%;background:var(--green)}
.main-nav{display:flex;gap:34px;font-size:13px;font-weight:500;text-transform:uppercase}
.main-nav a{color:var(--ink);text-decoration:none}
.main-nav a.active{color:var(--green)}

/* hero */
.hero{top:132px;height:417px;background:linear-gradient(100deg,#4f5b66 0%,#66737e 38%,#7f95ab 62%,#b9c4ce 100%)}
.hero-copy{position:absolute;left:90px;top:138px;width:640px;color:var(--white)}
.hero-copy h1{font-size:22px;font-weight:700;text-shadow:0 1px 4px rgba(0,0,0,.45);text-transform:uppercase}
.hero-copy p{font-size:13px;line-height:1.6;margin:12px 0 22px;text-shadow:0 1px 3px rgba(0,0,0,.5)}
.slider-dots{position:absolute;left:630px;top:360px;display:flex;gap:14px}
.slider-dots b{width:8px;height:8px;border-radius:50%;background:rgba(255,255,255,.6)}
.slider-dots b.on{background:var(--white)}

/* about */
.about{top:549px;height:359px}
.about-photo{position:absolute;left:150px;top:38px;width:250px;height:250px;border-radius:50%;background:radial-gradient(circle at 50% 40%,#f1ddd0,#b9a898 70%,#e2e2e2);border:6px solid #ececec}
.about-copy{position:absolute;left:590px;top:80px;width:520px}
.about-copy p{margin:14px 0 22px}

/* why us */
.why{top:908px;height:455px;background:var(--light)}
.why-intro{position:absolute;left:226px;top:38px;width:400px;text-align:center}
.why-intro p{margin-top:12px}
.feature{position:absolute;left:260px;width:420px;display:flex;align-items:flex-start;gap:22px}
.feature-text{flex:1;text-align:right}
.feature-text h3{font-size:12px;font-weight:700;color:var(--green);text-transform:uppercase;margin-bottom:6px}
.feature-icon{width:44px;height:44px;flex:none}
.why-photo{position:absolute;left:680px;top:40px;width:320px;height:415px;background:linear-gradient(180deg,#e9e9e9,#d9c5b6 45%,#5f9ec7 75%,#e3e3e3)}

/* services */
.services{top:1363px;height:416px;background:linear-gradient(180deg,#3c3c3c,#4d4035 70%,#5a4a3c);color:var(--white);text-align:center}
.services .heading{margin-top:50px;font-size:20px}
.services-intro{width:760px;margin:16px auto 0;font-size:11px;line-height:1.6;color:#e2e2e2}
.service-list{position:absolute;top:170px;left:0;width:1200px;display:flex;justify-content:center;gap:68px}
.service{width:134px}
.service-photo{width:134px;height:134px;border-radius:50%;border:3px solid var(--white)}
.service h4{font-size:12px;font-weight:500;margin-top:16px}

/* testimonials */
.testimonials{top:1779px;height:454px;text-align:center}
.testimonials .heading{margin-top:72px;font-size:17px;font-weight:500}
.client-photo{width:96px;height:96px;border-radius:50%;margin:42px auto 0;background:radial-gradient(circle at 50% 45%,#e7c9b4,#7a4f36 75%);border:4px solid #eee}
.quote{width:760px;margin:30px auto 0;font-size:13px;font-style:italic;line-height:1.7;color:var(--muted)}
.client-name{margin-top:14px;font-size:13px;font-weight:500;color:var(--green);text-transform:uppercase}
.testimonial-dots{display:flex;justify-content:center;gap:26px;margin-top:26px}
.testimonial-dots b{width:12px;height:12px;border-radius:50%;border:2px solid #bbb}
.testimonial-dots b.on{background:var(--green);border-color:var(--green)}

/* newsletter */
.newsletter{top:2233px;height:265px;background:var(--light);text-align:center}
.newsletter .heading{margin-top:68px;font-size:16px;font-weight:500}
.newsletter p{width:520px;margin:14px auto 0;font-size:11px;line-height:1.6;color:var(--muted)}
.subscribe{position:absolute;left:340px;top:190px;display:flex;gap:18px}
.subscribe .field{width:417px;height:38px;background:var(--white);border:1px solid #ddd}
.subscribe .btn{width:140px;height:38px;padding:0;line-height:38px;text-align:center}

/* footer */
.site-footer{top:2498px;height:303px;background:linear-gradient(180deg,#3e3e3e,#343434);color:var(--white)}
.footer-contact{position:absolute;left:190px;top:40px;width:380px}
.footer-contact h3,.footer-links h3,.footer-social h3{font-size:15px;font-weight:700;margin-bottom:10px}
.footer-contact p{font-size:10px;line-height:1.5;color:#d0d0d0;margin-bottom:12px}
.form-row{display:flex;gap:12px;margin-bottom:10px}
.input{height:24px;background:var(--white);color:#888;font-size:10px;padding:5px 8px;flex:1}
.input.tall{height:74px}
.send{background:var(--green);font-size:10px;font-weight:500;padding:6px 12px;display:inline-block}
.footer-links{position:absolute;left:688px;top:40px}
.footer-links li{list-style:none;font-size:12px;font-weight:500;line-height:2.1}
.footer-social{position:absolute;left:868px;top:40px}
.social-item{display:flex;align-items:center;gap:12px;font-size:12px;font-weight:500;margin-bottom:20px}
.social-item i{width:30px;height:30px;border-radius:50%;border:2px solid var(--white)}

.bottom-bar{position:absolute;left:0;top:2801px;width:1200px;height:38px;background:var(--green);color:var(--white);font-size:12px;display:flex;align-items:center;justify-content:center;gap:18px}
</style>
</head>
<body>

<div class="top-strip">
  <span><i></i>Mon – Sat: 8:00 – 18:00</span>
  <span><i></i>hello@plumrake.example</span>
  <span><i></i>+1 613 555 0142</span>
  <span><i></i>Ottawa, Canada</span>
</div>

<header class="site-header">
  <div class="brand"><span class="brand-dot"></span>Tidewell Housekeeping</div>
  <nav class="main-nav">
    <a class="active" href="#">Home</a>
    <a href="#">About Us</a>
    <a href="#">Services</a>
    <a href="#">Contact Us</a>
    <a href="#">Login / Signup</a>
  </nav>
</header>

<section class="hero" role="img" aria-label="Photo of a gloved hand polishing a chrome kitchen tap with a yellow cloth">
  <div class="hero-copy">
    <h1>Welcome to Tidewell Housekeeping Services</h1>
    <p>Eco-friendly cleaning for homes and offices across Ottawa. Gentle products, careful hands,<br>and all our own gear and supplies brought to your door every single visit.</p>
    <span class="btn">Read More</span>
  </div>
  <div class="slider-dots"><b class="on"></b><b></b><b></b><b></b></div>
</section>

<section class="about">
  <div class="about-photo" role="img" aria-label="Portrait of a smiling cleaner holding a spray bottle"></div>
  <div class="about-copy">
    <h2 class="heading">About Us</h2>
    <p class="small">We are a new Ottawa housekeeping team built on care and clean habits. Every product we use is kind to the planet and gentle on sensitive skin. We wash windows, walls, kitchens and bathrooms, dust, vacuum and scrub floors by hand, so your home and your pets can breathe easy after every visit we make.</p>
    <span class="btn">Read More</span>
  </div>
</section>

<section class="why">
  <div class="why-intro">
    <h2 class="heading">Why We Are Different</h2>
    <p class="small">We treat each home as our own, with safe supplies, steady people and a plan that fits the way you live.</p>
  </div>

  <div class="feature" style="top:160px">
    <div class="feature-text">
      <h3>Personal Approach</h3>
      <p class="small">We learn your rooms, your pets and your routine, then shape every visit around them.</p>
    </div>
    <svg class="feature-icon" viewBox="0 0 44 44" fill="none" stroke="var(--green)" stroke-width="2"><circle cx="22" cy="22" r="20"/><circle cx="22" cy="17" r="6"/><path d="M11 34c3-6 19-6 22 0"/></svg>
  </div>

  <div class="feature" style="top:262px">
    <div class="feature-text">
      <h3>Friendly</h3>
      <p class="small">Warm, trusted people who arrive on time and leave every room calm and fresh.</p>
    </div>
    <svg class="feature-icon" viewBox="0 0 44 44" fill="none" stroke="var(--green)" stroke-width="2"><circle cx="22" cy="22" r="20"/><circle cx="22" cy="22" r="8"/><path d="M22 6v6M22 32v6M6 22h6M32 22h6"/></svg>
  </div>

  <div class="feature" style="top:350px">
    <div class="feature-text">
      <h3>Value</h3>
      <p class="small">Fair, clear prices with no hidden fees and all supplies included.</p>
    </div>
    <svg class="feature-icon" viewBox="0 0 44 44" fill="none" stroke="var(--green)" stroke-width="2"><circle cx="22" cy="22" r="20"/><path d="M14 22l6 6 10-12"/></svg>
  </div>

  <div class="why-photo" role="img" aria-label="Photo of a smiling cleaner in yellow gloves and blue top"></div>
</section>

<section class="services" role="img" aria-label="Dark photo of a cleaned wooden floor behind the services">
  <h2 class="heading">Our Services</h2>
  <p class="services-intro">From a quick weekly tidy to a full deep clean, we cover every room with safe, green products. Choose a service below or mix them into one plan that suits your home, your office and your pets.</p>
  <div class="service-list">
    <div class="service"><div class="service-photo" role="img" aria-label="Home cleaning photo" style="background:radial-gradient(#d9c9a5,#8a7a55)"></div><h4>Home cleaning</h4></div>
    <div class="service"><div class="service-photo" role="img" aria-label="Window cleaning photo" style="background:radial-gradient(#f3e36a,#5b8fc9)"></div><h4>Window cleaning</h4></div>
    <div class="service"><div class="service-photo" role="img" aria-label="Kitchen cleaning photo" style="background:radial-gradient(#f0d3c0,#6d8fb3)"></div><h4>Kitchen cleaning</h4></div>
    <div class="service"><div class="service-photo" role="img" aria-label="Bathroom cleaning photo" style="background:radial-gradient(#f2e4d8,#b5a497)"></div><h4>Bathroom cleaning</h4></div>
    <div class="service"><div class="service-photo" role="img" aria-label="Office cleaning photo" style="background:radial-gradient(#e5d160,#4d4d4d)"></div><h4>Office cleaning</h4></div>
  </div>
</section>

<section class="testimonials">
  <h2 class="heading">What Our Clients Says</h2>
  <div class="client-photo" role="img" aria-label="Client portrait"></div>
  <p class="quote">Our house has never felt this fresh, and the cats did not mind a thing. The team is careful, kind and always on time, and I love knowing every product they use is safe for us and for the planet.</p>
  <p class="client-name">Marla Quinton</p>
  <div class="testimonial-dots"><b></b><b class="on"></b><b></b></div>
</section>

<section class="newsletter">
  <h2 class="heading">Subscribe for Newsletter</h2>
  <p>Get green cleaning tips, seasonal offers and news from our team.<br>One short email a month, and you can leave the list at any time.</p>
  <div class="subscribe">
    <div class="field"></div>
    <span class="btn">Subscribe</span>
  </div>
</section>

<footer class="site-footer">
  <div class="footer-contact">
    <h3>Contact</h3>
    <p>Send us a note and we will reply within one business day to plan your first visit.</p>
    <div class="form-row"><div class="input">First Name</div><div class="input">Last Name</div></div>
    <div class="form-row"><div class="input">Email</div></div>
    <div class="form-row"><div class="input tall">Your Message</div></div>
    <span class="send">Send Message</span>
  </div>
  <div class="footer-links">
    <h3>Links</h3>
    <ul>
      <li>Home</li><li>What we do</li><li>About Us</li><li>policies</li><li>Services</li><li>Contact Us</li>
    </ul>
  </div>
  <div class="footer-social">
    <h3>Social Media</h3>
    <div class="social-item"><i></i>Friendwall</div>
    <div class="social-item"><i></i>Careerlink</div>
    <div class="social-item"><i></i>Circlespace</div>
  </div>
</footer>

<div class="bottom-bar"><span>hello@plumrake.example</span><span>|</span><span>© Copyright 2017</span></div>

</body>
</html>
```